New Web Page Design - Cement Rendering Business

Looking for a overhaul of our existing website (www.norpex.com.au).

Looking for a sleek and elegant design that incorporates the colours of our logos, black / green and white. Needs to look professional and want it to be well above what our competition is offering. (Findora search for 'cement rendering sydney' will display the competition we want to be well ahead of.

Prefer a mixture of pages with black background and white alternatively between home (black), about us (white), contact us (black) and gallery (white).

Would like to incorporate our logo on all pages attached preferably in the top left corner.

Website needs to be search engine optimised and have easily updated photo gallery which we already have.

Also need to embed our trackwise metrics code on the front home page.

Website needs to be able easily updated (text, pictures ) as required.
content management system should include fields where you can alter your page titles, meta description and keywords.

Pages also needs to be optimised for mobile devices, iphone, ipad and other mobile devices. (it is a current feature we have)

If you have any questions, just message me.

Please remember the look and feel of the site is important to us, we don't want it over complicated, simple elegant and professional in line with our logo standards.
Updates

Hi All, As an example of the look and feel we like. We have found a site that may assist in your design and creative process. http://demo.quorvix.org/ We like the simplicity, elegance and professional look of this site, although we would like it with our images, colours and logos. I hope this helps.! keep the great designs coming!

All, Thanks for the designs. Please try and use our website images due to copyright reasons for all your designs. Tomas

Target Market(s)

Construction Companies

Industry/Entity Type

Business

Colors
9bcb3b
acd036
474747

Requirements
Must have
• Search Engine Optimised.
Photo Gallery
Elegant/Professional Look & Feel.
Simple Yet Effective
Nice to have
• Moving Parts
Should not have
• Overly Complicated.
Cheap & Traditional Looking.
Boring

```html
<!DOCTYPE html>
<html lang="en">
<head>
<meta charset="utf-8">
<title>Norpex – Cement Rendering</title>
<link rel="stylesheet" href="https://fonts.googleapis.com/css2?family=Open+Sans:wght@300;400;600;700&display=swap">
<style>
:root{
  --green:#9bcb3b;
  --green-bright:#acd036;
  --charcoal:#474747;
  --charcoal-deep:#2b2b2b;
  --charcoal-bar:#3b3b3b;
  --panel-light:#e6e4e4;
  --ink:#222222;
  --white:#ffffff;
  --muted:#bdbdbd;
  --line:#8a8a8a;
}
*{box-sizing:border-box;margin:0;padding:0}
html,body{width:1200px;height:2428px;overflow:hidden}
body{position:relative;background:var(--charcoal);font-family:"Open Sans",Arial,sans-serif;color:var(--white)}
.abs{position:absolute}
.photo{position:absolute;display:block}

/* header */
.site-header{left:0;top:0;width:1200px;height:118px;background:var(--charcoal);border-top:3px solid var(--green)}
.brand{left:110px;top:20px;display:flex;align-items:center;gap:18px}
.brand-mark{width:72px;height:72px;border-radius:50%;background:var(--green)}
.brand-name{font-size:42px;font-weight:300;color:var(--green);line-height:1;letter-spacing:1px}
.brand-tag{font-size:11px;color:var(--muted);margin-top:4px}
.nav-link{position:absolute;top:0;height:112px;line-height:112px;font-size:13px;font-weight:600;color:var(--white);text-decoration:none;white-space:nowrap}
.nav-link.is-active{background:var(--green);width:68px;text-align:center}

/* hero */
.hero{left:0;top:118px;width:1200px;height:499px;
  background:
    radial-gradient(ellipse 260px 90px at 440px 200px,rgba(255,255,255,.75),transparent 70%),
    radial-gradient(ellipse 300px 80px at 1050px 120px,rgba(255,255,255,.6),transparent 70%),
    radial-gradient(ellipse 220px 70px at 160px 140px,rgba(255,255,255,.55),transparent 70%),
    radial-gradient(ellipse 200px 220px at 850px 220px,rgba(70,70,80,.55),transparent 70%),
    linear-gradient(180deg,#5f95cf 0%,#a9c8e8 45%,#cfd6dc 70%,#8c8c88 100%)}
.hero-arrow{top:296px;width:57px;height:56px;background:rgba(70,70,70,.8)}
.hero-arrow svg{display:block;margin:16px auto}

/* features */
.feature{width:322px}
.feature-body{position:relative;height:178px;padding:20px 14px;background:var(--panel-light);color:var(--ink)}
.feature-body.is-green{background:var(--green);color:var(--white)}
.feature-title{font-size:24px;font-weight:700;margin-bottom:12px}
.feature-text{font-size:13px;line-height:1.35}
.btn{display:inline-block;font-size:13px;padding:6px 12px;text-decoration:none;white-space:nowrap}
.btn-light{background:#ececec;color:var(--ink)}
.btn-dark{background:#2f2f2f;color:var(--white)}
.btn-green{background:var(--green);color:var(--white)}
.feature .btn{position:absolute;right:14px;top:134px}
.feature-photo{position:relative;height:181px}

/* newsletter */
.newsletter{left:99px;top:866px;width:1002px;height:114px;background:var(--green)}
.newsletter-icon{position:absolute;left:14px;top:35px}
.newsletter-title{position:absolute;left:69px;top:38px;font-size:26px;font-weight:400;white-space:nowrap}
.newsletter-text{position:absolute;left:399px;top:32px;width:270px;font-size:13px;line-height:1.3}
.newsletter-field{position:absolute;left:676px;top:41px;width:217px;height:32px;background:#d6e9a8;color:#7a8a5a;font-size:13px;padding:7px 12px}
.newsletter-submit{position:absolute;left:899px;top:41px;width:89px;height:32px;text-align:center;padding:6px 0}

/* offer */
.offer{left:0;top:1036px;width:1200px;height:526px;background:var(--charcoal-deep)}
.offer-heading{top:1064px;left:0;width:1200px;text-align:center;font-size:31px;font-weight:600}
.offer-heading span{color:var(--green)}
.offer-sub{top:1105px;left:0;width:1200px;text-align:center;font-size:14px;color:#9a9a9a}
.offer-card{top:1148px;width:312px}
.offer-photo{position:relative;height:206px}
.offer-card h3{font-size:15px;font-weight:700;color:var(--green);margin:24px 0 6px}
.offer-card p{font-size:14px;line-height:1.35;margin-bottom:18px}

/* gallery */
.gallery{left:0;top:1562px;width:1200px;height:486px;
  background:
    radial-gradient(ellipse 260px 300px at 1060px 220px,rgba(180,110,70,.8),transparent 70%),
    radial-gradient(ellipse 200px 160px at 430px 120px,rgba(160,180,90,.35),transparent 70%),
    linear-gradient(90deg,#3c3a34 0%,#6b6357 40%,#8d7a68 70%,#a4765d 100%)}
.gallery-feature{left:115px;top:1621px;width:231px;height:375px;border:3px solid var(--white);
  background:linear-gradient(180deg,#b44a34 0%,#b44a34 10%,#d8d6d1 14%,#e2e0db 60%,#8c8a84 100%)}
.gallery-caption{position:absolute;left:0;bottom:0;width:100%;padding:10px 12px 14px;background:rgba(30,30,30,.55)}
.gallery-caption strong{display:block;font-size:21px;font-weight:400;line-height:1.1}
.gallery-caption span{font-size:12.5px;line-height:1.3;display:block;margin-top:6px}
.gallery-title{left:362px;top:1614px;font-size:32px;font-weight:400}
.gallery-tab{position:absolute;top:1696px;height:24px;font-size:12px;line-height:24px;text-align:center;background:rgba(40,40,40,.7)}
.gallery-tab.is-active{background:var(--green-bright)}
.thumb{width:172px;height:112px;border:2px solid var(--white)}

/* footer */
.footer-heading{font-size:18px;color:var(--green);font-weight:400}
.social{display:flex;gap:12px;margin-top:20px}
.social i{display:block;width:38px;height:38px;border-radius:50%;background:#5e5e5e}
.social i.is-green{background:var(--green)}
.blog-title{font-size:13px;font-weight:600;margin-top:14px}
.blog-date{font-size:9px;color:var(--green)}
.blog-text{font-size:12.5px;line-height:1.4;margin-top:4px}
.blog-more{font-size:12.5px;color:var(--green);margin-top:6px}
.ad-list{list-style:none;width:273px;margin-top:14px}
.ad-list li{font-size:11px;height:25px;line-height:22px;border-bottom:2px solid var(--line);padding-left:10px}
.contact-field{width:275px;height:30px;background:#e8e4e4;color:#888;font-size:12px;padding:6px 10px;margin-top:10px}
.contact-field.is-tall{height:114px}
.contact-submit{margin-top:10px;width:74px;height:28px;background:var(--green);font-size:12px;font-weight:700;text-align:center;line-height:28px}
.copyright{left:0;top:2368px;width:1200px;height:60px;background:var(--charcoal-bar);border-top:2px solid #5a5a5a;font-size:11px;padding:22px 109px}
</style>
</head>
<body>

<header class="abs site-header">
  <div class="abs brand">
    <span class="brand-mark"></span>
    <div>
      <div class="brand-name">NORPEX</div>
      <div class="brand-tag">Cement Rendering</div>
    </div>
  </div>
  <nav>
    <a class="nav-link is-active" href="#" style="left:576px">HOME</a>
    <a class="nav-link" href="#" style="left:662px">ABOUT US</a>
    <a class="nav-link" href="#" style="left:755px">PROJECTS</a>
    <a class="nav-link" href="#" style="left:842px">SERVICES</a>
    <a class="nav-link" href="#" style="left:931px">GALLERY</a>
    <a class="nav-link" href="#" style="left:1016px">CONTACT</a>
  </nav>
</header>

<div class="photo hero" role="img" aria-label="Two engineers in hard hats reading plans in front of a crane and blue sky"></div>
<div class="abs hero-arrow" style="left:0"><svg width="14" height="24" viewBox="0 0 14 24"><path d="M12 2 2 12l10 10" fill="none" stroke="#fff" stroke-width="2.5"/></svg></div>
<div class="abs hero-arrow" style="left:1143px"><svg width="14" height="24" viewBox="0 0 14 24"><path d="M2 2l10 10L2 22" fill="none" stroke="#fff" stroke-width="2.5"/></svg></div>

<section>
  <article class="abs feature" style="left:99px;top:441px">
    <div class="feature-body is-green">
      <h2 class="feature-title">TECHNOLOGY</h2>
      <p class="feature-text">consectetur adipisicing elit, sed do eiusmod tempor incididunt ut labore et dolore magna aliqua.</p>
      <a class="btn btn-light" href="#">Read More</a>
    </div>
    <div class="photo feature-photo" style="background:linear-gradient(135deg,#e8f1f8 0%,#9cc7dd 25%,#2f9ab8 55%,#16506a 100%)" role="img" aria-label="Glass office tower facade"></div>
  </article>
  <article class="abs feature" style="left:439px;top:441px">
    <div class="feature-body">
      <h2 class="feature-title">QUALITY</h2>
      <p class="feature-text">consectetur adipisicing elit, sed do eiusmod tempor incididunt ut labore et dolore magna aliqua.</p>
      <a class="btn btn-dark" href="#">Read More</a>
    </div>
    <div class="photo feature-photo" style="background:linear-gradient(180deg,#9a9890 0%,#c9c5bc 40%,#e4e2de 70%,#9fa4aa 100%)" role="img" aria-label="Businessman on the phone at a building site"></div>
  </article>
  <article class="abs feature" style="left:779px;top:441px">
    <div class="feature-body">
      <h2 class="feature-title">THE STAFF</h2>
      <p class="feature-text">consectetur adipisicing elit, sed do eiusmod tempor incididunt ut labore et dolore magna aliqua.</p>
      <a class="btn btn-dark" href="#">Read More</a>
    </div>
    <div class="photo feature-photo" style="background:linear-gradient(90deg,#c4c6c8 0%,#9da0a3 35%,#a88c7c 60%,#2c3444 100%)" role="img" aria-label="Worker in a white hard hat at an industrial plant"></div>
  </article>
</section>

<section class="abs newsletter">
  <svg class="newsletter-icon" width="46" height="40" viewBox="0 0 46 40"><path d="M2 20 44 2 34 38 22 26 2 20Z M22 26 44 2" fill="none" stroke="#fff" stroke-width="2.5" stroke-linejoin="round"/></svg>
  <h2 class="newsletter-title">Subscribe To Newsletter</h2>
  <p class="newsletter-text">Lorem ipsum dolor sit amet, consectetur adipisicing elit, sed do eiusmod tempor incididunt ut labore</p>
  <div class="newsletter-field">Email</div>
  <a class="btn btn-dark newsletter-submit" href="#">Submit</a>
</section>

<section class="abs offer"></section>
<h2 class="abs offer-heading">What We <span>Offer</span></h2>
<p class="abs offer-sub">Praesent justo dolor, lobortis quis, lobortis dignissim, pulvinar ac, lorem</p>
<article class="abs offer-card" style="left:99px">
  <div class="photo offer-photo" style="background:linear-gradient(180deg,#d7dce0 0%,#b8bdc0 40%,#c9b24a 62%,#b3473c 85%,#7a2f2a 100%)" role="img" aria-label="Industrial pipework with yellow valves"></div>
  <h3>Lorem ipsum dolor sit amet</h3>
  <p>Lorem ipsum dolor sit amet, consectetur adipisicing elit, sed do eiusmod tempor incididunt ut labore</p>
  <a class="btn btn-green" href="#">Read More</a>
</article>
<article class="abs offer-card" style="left:443px">
  <div class="photo offer-photo" style="background:linear-gradient(160deg,#a9cde9 0%,#d9b36a 45%,#c08a3e 75%,#8a5f2c 100%)" role="img" aria-label="Timber roof trusses against the sky"></div>
  <h3>Blanditiis praesentium</h3>
  <p>Lorem ipsum dolor sit amet, consectetur adipisicing elit, sed do eiusmod tempor incididunt ut labore</p>
  <a class="btn btn-light" href="#">Read More</a>
</article>
<article class="abs offer-card" style="left:787px">
  <div class="photo offer-photo" style="background:linear-gradient(135deg,#7d7f81 0%,#b9babb 45%,#d8d8d6 60%,#e68a3a 80%,#c46a2a 100%)" role="img" aria-label="Gloved hand rendering a wall with a trowel"></div>
  <h3>Eligendi optio</h3>
  <p>Lorem ipsum dolor sit amet, consectetur adipisicing elit, sed do eiusmod tempor incididunt ut labore</p>
  <a class="btn btn-light" href="#">Read More</a>
</article>

<section class="photo gallery" role="img" aria-label="Blurred building site with a brick wall"></section>
<div class="abs gallery-feature" role="img" aria-label="Freshly rendered house wall under a tiled roof">
  <div class="gallery-caption">
    <strong>Norpex constructions</strong>
    <span>We Export our product all around the world internationally.</span>
  </div>
</div>
<h2 class="abs gallery-title">Product Gallery</h2>
<span class="gallery-tab is-active" style="left:364px;width:57px">ALL</span>
<span class="gallery-tab" style="left:447px;width:96px">Work 1</span>
<span class="gallery-tab" style="left:570px;width:96px">Work 2</span>
<div class="photo thumb" style="left:366px;top:1759px;background:linear-gradient(135deg,#c4c7c8 0%,#a7b38a 50%,#9fc34a 100%)" role="img" aria-label="Render being applied to a wall"></div>
<div class="photo thumb" style="left:555px;top:1759px;background:linear-gradient(180deg,#6d7a86 0%,#eeeeec 50%,#cfcfcc 70%,#5b5b55 100%)" role="img" aria-label="White work van"></div>
<div class="photo thumb" style="left:743px;top:1759px;background:linear-gradient(135deg,#c46a4a 0%,#a9a6a0 60%,#8e8c87 100%)" role="img" aria-label="Trowel smoothing render"></div>
<div class="photo thumb" style="left:929px;top:1759px;background:linear-gradient(135deg,#8e8b84 0%,#a9a79e 40%,#d4df3a 60%,#5d5a55 100%)" role="img" aria-label="Worker in hi-vis rendering a wall"></div>
<div class="photo thumb" style="left:366px;top:1884px;background:linear-gradient(90deg,#a9b6c0 0%,#d7dcdf 50%,#e6e5e1 100%)" role="img" aria-label="Rendered wall corner"></div>
<div class="photo thumb" style="left:555px;top:1884px;background:linear-gradient(180deg,#7ea7cf 0%,#e2d7c2 45%,#caa778 70%,#5d4a36 100%)" role="img" aria-label="House under construction"></div>
<div class="photo thumb" style="left:743px;top:1884px;background:linear-gradient(135deg,#9c9c98 0%,#c9c6bd 55%,#e0c43a 80%,#9c8a40 100%)" role="img" aria-label="Trowel on a smooth render surface"></div>
<div class="photo thumb" style="left:929px;top:1884px;background:linear-gradient(90deg,#e0ddd6 0%,#cfcbc3 50%,#9f9c95 100%)" role="img" aria-label="Finished rendered wall"></div>

<footer>
  <div class="abs" style="left:109px;top:2074px;width:280px">
    <h3 class="footer-heading">SOCIAL LINKS</h3>
    <div class="social"><i class="is-green" aria-label="Social link"></i><i aria-label="Social link"></i><i aria-label="Social link"></i></div>
    <h3 class="footer-heading" style="margin-top:40px">BLOGS</h3>
    <p class="blog-title">Post Title</p>
    <p class="blog-date">Friday, 6th April 2014</p>
    <p class="blog-text">Lorem ipsum dolor sit amet, consectetur adipiscing elit. Nunc non diam erat. In fringilla massa ut nisi ullamcorper pellentesque.</p>
    <p class="blog-more">Read More »</p>
  </div>
  <div class="abs" style="left:447px;top:2074px">
    <h3 class="footer-heading">ADVERTISE WITH US</h3>
    <ul class="ad-list">
      <li>Lorem ipsum dolor sit</li>
      <li>Amet consectetur</li>
      <li>Praesent vel sem id</li>
      <li>Curabitur hendrerit est</li>
      <li>Aliquam eget erat nec sapien</li>
      <li>Cras id augue nunc</li>
      <li>In nec justo non</li>
      <li>Vivamus mollis enim ut</li>
      <li>Curabitur hendrerit est</li>
    </ul>
  </div>
  <div class="abs" style="left:820px;top:2074px">
    <h3 class="footer-heading">CONTACT US</h3>
    <div class="contact-field">Name</div>
    <div class="contact-field">Email</div>
    <div class="contact-field is-tall">Messages</div>
    <div class="contact-submit">SUBMIT</div>
  </div>
  <div class="abs copyright">Copyright © 2014 - All Rights Reserved</div>
</footer>

</body>
</html>
```